Fall Convention Graphic Designs (logo, digital brochure, t-shirt designs, social media templates)

I need a graphic package for the Brightwell Dance Guild Fall Dance Convention. Brightwell Dance Guild is a non-profit organization of dance teachers, and this educational dance conference is for members and their students with multiple events throughout the weekend. The convention has a new them each year. I will need a package with a general "logo" type graphic, a digital brochure, t-shirt design, and social media graphic templates. This year's Convention has a general theme and names for each event throughout the weekend.
The theme and event names for this year are:
Convention Theme Tales in Motion: Beneath a Silver Sky
Registration Desk The Willow Nook
Members Welcome A Golden Greeting
Banquet A Velvet Soiree
President's Reception Glow Beyond Dusk
Jr. Member Desk Wanderers' Wharf
Jr. Member Pizza Party Meadow Mixer
Members Luncheon Harbor Reveries

I am attaching a word file that includes information and text to be included in brochure. Also attached are designs from previous years for brochures, T-shirts, and social media graphics.

Colors that we will be using for decorations at various events over the weekend this year are shades of green (fern and mossy green), shades of blue (including navy), white, and pinks (including mauve). The banquet event will be decorated as an enchanted forest. We are using fairy lights, books that look like a storybook, and lanterns for decorations as well. I think I would like a more modern design, and I do not want anything that is childish or too whimsical. While we are using floral decorations I don't want bunches of flowers in the design.

*I am open to seeing initial logo type designs and giving feedback to make sure it is a direction that I like and then moving forward with the other parts of the project.

```html
<!DOCTYPE html>
<html lang="en">
<head>
<meta charset="UTF-8">
<title>Brightwell Dance Guild Fall Convention</title>
<link href="https://fonts.googleapis.com/css2?family=EB+Garamond:wght@400;500&family=Playfair+Display:wght@700;800&family=Great+Vibes&display=swap" rel="stylesheet">
<style>
  :root {
    --forest-deep: #0c1a11;
    --forest-mid: #1f4a32;
    --forest-glow: #5fa57f;
    --text-white: #ffffff;
    --gold: #f3d35f;
    --lantern-cream: #ffe3b8;
    --lantern-glow: #ff9d2e;
  }
  * { margin: 0; padding: 0; box-sizing: border-box; }
  html, body {
    width: 927px; height: 1200px; overflow: hidden;
    background: var(--forest-deep);
  }
  .poster {
    position: relative;
    width: 927px; height: 1200px;
    overflow: hidden;
    font-family: "EB Garamond", Georgia, serif;
    color: var(--text-white);
  }
  .forest-scene {
    position: absolute; inset: 0;
    background:
      radial-gradient(ellipse 48% 30% at 25% 78%, rgba(255,150,40,0.22), transparent 70%),
      radial-gradient(ellipse 30% 20% at 85% 80%, rgba(255,150,40,0.18), transparent 70%),
      radial-gradient(ellipse 55% 50% at 50% 38%, var(--forest-glow) 0%, var(--forest-mid) 55%, var(--forest-deep) 100%);
  }
  .header {
    position: absolute; left: 0; right: 0; top: 270px;
    text-align: center;
  }
  .org-name {
    font-size: 15px; letter-spacing: 0.5px; text-transform: uppercase;
  }
  .event-type {
    margin-top: 8px;
    font-size: 33px; letter-spacing: 0.5px;
  }
  .theme-title {
    position: absolute; left: 0; right: 0; top: 368px;
    display: flex; justify-content: center; align-items: center; gap: 12px;
    font-family: "Playfair Display", Georgia, serif; font-weight: 800;
  }
  .theme-title .small-words {
    font-size: 31px; line-height: 0.95; text-align: left;
  }
  .theme-title .big-word {
    font-size: 80px; line-height: 1;
  }
  .theme-sub {
    position: absolute; left: 0; right: 0; top: 458px;
    text-align: center;
    font-family: "Playfair Display", Georgia, serif; font-weight: 700;
    font-size: 29px; letter-spacing: 9px; color: var(--gold);
  }
  .theme-script {
    position: absolute; left: 0; right: 0; top: 488px;
    text-align: center;
    font-family: "Great Vibes", cursive;
    font-size: 100px; color: var(--lantern-cream);
    text-shadow: 0 0 10px var(--lantern-glow), 0 0 22px rgba(255,157,46,0.6);
  }
  .event-date {
    position: absolute; left: 0; right: 0; top: 642px;
    text-align: center; font-size: 41px;
  }
  .venue {
    position: absolute; left: 0; right: 0; top: 712px;
    text-align: center; font-size: 25px; line-height: 31px;
    text-transform: uppercase; letter-spacing: 0.5px;
  }
  .lodging {
    position: absolute; left: 45px; top: 1038px;
  }
  .lodging-label {
    font-size: 14px; line-height: 17px; text-transform: uppercase; letter-spacing: 0.3px;
  }
  .lodging-address {
    margin-top: 10px; font-size: 16.5px; line-height: 19.5px;
  }
</style>
</head>
<body>
  <main class="poster">
    <div class="forest-scene" role="img" aria-label="Enchanted forest at night framed by twisting branches hung with glowing fairy lights, with glowing spotted mushrooms and mossy stones along the ground"></div>

    <header class="header">
      <p class="org-name">Brightwell Dance Guild, Inc.</p>
      <p class="event-type">Fall Convention</p>
    </header>

    <h1 class="theme-title">
      <span class="small-words">Tales<br>in</span>
      <span class="big-word">Motion</span>
    </h1>
    <p class="theme-sub">BENEATH A</p>
    <p class="theme-script">Silver Sky</p>

    <p class="event-date">November 19 – 22, 2026</p>
    <p class="venue">Halden Convention Center<br>Ashgrove Grand Hotel<br>Millbrook, NC</p>

    <section class="lodging">
      <p class="lodging-label">Outstanding<br>Accommodations at the</p>
      <p class="lodging-address">Ashgrove Grand Hotel<br>4580 Larkspur Avenue,<br>Millbrook, NC 27590</p>
    </section>
  </main>
</body>
</html>
```